Copper Meadow Creamery Business cards

We need a logo design for our family dairy. Included on the cards should be my name/my husbands name/the dairy name/ all the phone numbers/address and email. The name is Copper Meadow Creamery, LLC. We would like to use our farm mascot pic on the card. We know the pictures I sent you are of a beef cow but she is the mascot of the farm. We were thinking that maybe put a picture of her head in the middle of the card with a "B" on one side and a "D" on the other side with a "C" around the picture of the cow. But we are open to any ideas. We are looking for something kind of professional and a design that that can be used on cards, clothing and a car sign. Black lettering and blue for the other color...or what looks good.

Target Market(s)

All

Industry/Entity Type

Farming

Contact Information for Business Card

Marla Dutton Owner (555)417-2093
Ronald Pfister Owner (555)238-7715
Copper Meadow Creamery, LLC (555)906-4182
Coppermeadowcreamery@mailbarn.test
7126 County Lane 91, Harrowvale, IA 50917

Font styles to use
Sans Serif

Colors
3176b5
3c7bb8
3277b5
0255a3

Requirements
Must have
• Some design that incorporates a drawing/pic of the cow pictures that were sent.
Nice to have
• no suggestions
Should not have
• no suggestions

```html
<!DOCTYPE html>
<html lang="en">
<head>
<meta charset="utf-8">
<title>Copper Meadow Creamery – Business Cards</title>
<link rel="stylesheet" href="https://fonts.googleapis.com/css2?family=Tinos:wght@400&display=swap">
<style>
  :root {
    --page-bg: #d6d6d6;
    --card-bg: #ffffff;
    --ink: #1a1a1a;
    --muted-rule: #9a9a9a;
    --accent-blue: #3aaee6;
    --silver-light: #f7f6f1;
    --silver-mid: #e4e2d8;
    --silver-warm: #ecebe0;
  }
  * { box-sizing: border-box; margin: 0; padding: 0; }
  html, body {
    width: 1200px; height: 800px; overflow: hidden;
    background: var(--page-bg);
    font-family: "Tinos", "Times New Roman", serif;
    color: var(--ink);
  }
  .sheet {
    position: relative; width: 1200px; height: 800px;
    display: flex; align-items: center; justify-content: center; gap: 60px;
  }
  .card {
    position: relative; width: 520px; height: 298px;
    background: var(--card-bg);
    box-shadow: 0 2px 6px rgba(0,0,0,.12);
    overflow: hidden;
  }
  .card--front .silver-band {
    position: absolute; left: 0; right: 0; top: 22px; height: 232px;
    background: linear-gradient(100deg, var(--silver-mid) 0%, var(--silver-light) 35%, var(--silver-warm) 55%, var(--silver-light) 72%, var(--silver-mid) 100%);
  }
  .card--back .accent-line {
    position: absolute; left: 0; right: 0; top: 40px; height: 5px;
    background: var(--accent-blue);
  }
  .brand {
    position: absolute; left: 0; right: 0; top: 72px;
    display: flex; flex-direction: column; align-items: center;
  }
  .brand-row { display: flex; align-items: center; gap: 10px; }
  .brand-dot {
    width: 34px; height: 34px; border-radius: 50%;
    border: 3px solid var(--ink);
  }
  .brand-name { font-size: 26px; letter-spacing: .5px; color: var(--ink); }
  .brand-rule { width: 230px; height: 1px; background: var(--muted-rule); margin-top: 8px; }
  .contact {
    position: absolute; left: 44px; top: 150px;
    font-size: 13.5px; line-height: 19px;
  }
  .contact-line { display: flex; align-items: center; gap: 7px; white-space: nowrap; }
  .contact-line--indent { padding-left: 19px; }
  .icon { width: 12px; height: 12px; flex: none; }
</style>
</head>
<body>
<main class="sheet">

  <section class="card card--front" aria-label="Business card, silver front">
    <div class="silver-band"></div>
    <div class="brand">
      <div class="brand-row">
        <span class="brand-dot"></span>
        <span class="brand-name">Copper Meadow Creamery</span>
      </div>
      <div class="brand-rule"></div>
    </div>
    <div class="contact">
      <p class="contact-line">
        <svg class="icon" viewBox="0 0 12 12" aria-hidden="true"><rect width="12" height="12" fill="#1a1a1a"/><path d="M3.2 2.5l1.4 0 .6 1.6-.9.7c.4.9 1 1.5 1.9 1.9l.7-.9 1.6.6 0 1.4c-3 .3-5.6-2.3-5.3-5.3z" fill="#fff"/></svg>
        Marla Dutton (555)417-2093 / Ronald Pfister (555)238-7715
      </p>
      <p class="contact-line contact-line--indent">Copper Meadow Creamery, LLC (555)906-4182</p>
      <p class="contact-line">
        <svg class="icon" viewBox="0 0 12 12" aria-hidden="true"><rect width="12" height="12" fill="#1a1a1a"/><rect x="3" y="3" width="6" height="6" fill="#fff"/></svg>
        Coppermeadowcreamery@mailbarn.test
      </p>
      <p class="contact-line">7126 County Lane 91, Harrowvale, IA 50917</p>
    </div>
  </section>

  <section class="card card--back" aria-label="Business card, white with blue line">
    <div class="accent-line"></div>
    <div class="brand">
      <div class="brand-row">
        <span class="brand-dot"></span>
        <span class="brand-name">Copper Meadow Creamery</span>
      </div>
      <div class="brand-rule"></div>
    </div>
    <div class="contact">
      <p class="contact-line">
        <svg class="icon" viewBox="0 0 12 12" aria-hidden="true"><rect width="12" height="12" fill="#1a1a1a"/><path d="M3.2 2.5l1.4 0 .6 1.6-.9.7c.4.9 1 1.5 1.9 1.9l.7-.9 1.6.6 0 1.4c-3 .3-5.6-2.3-5.3-5.3z" fill="#fff"/></svg>
        Marla Dutton (555)417-2093 / Ronald Pfister (555)238-7715
      </p>
      <p class="contact-line contact-line--indent">Copper Meadow Creamery, LLC (555)906-4182</p>
      <p class="contact-line">
        <svg class="icon" viewBox="0 0 12 12" aria-hidden="true"><rect width="12" height="12" fill="#1a1a1a"/><rect x="3" y="3" width="6" height="6" fill="#fff"/></svg>
        Coppermeadowcreamery@mailbarn.test
      </p>
      <p class="contact-line">7126 County Lane 91, Harrowvale, IA 50917</p>
    </div>
  </section>

</main>
</body>
</html>
```